New Snazzy yet professinoal business card updated for todays consumer for a Real Estate Professional

I work in a family owned real estate business where we specialize in sales (buyer/seller) and property management. I would like a snazzy business card that will set me apart from other agents while maintaining its professional appearance. I would like to use the front and back of the card incorporating the business logo on the front with pictures and my personal logo on the back side. I have to have the TPXN symbol which I have attached. Card must be easy to read, distinguishable, and professional. Old card with contact information attached. My email has changed to Milo@MiloBrentwickHomes.com

Target Market(s)

Home Sellers, Home Buyers, Business Professionals, Marketing Services,

Industry/Entity Type

Real Estate Agent

Contact Information for Business Card

Professional business card to stand apart from other agents while maintaining a professional appeal.

Font styles to use
Serif

Colors
ec1f27
fbee3e
0455a3

Requirements
Must have
• Must have contact information clear, easy to read. legible
Nice to have
• My picture.

```html
<!DOCTYPE html>
<html lang="en">
<head>
<meta charset="utf-8">
<title>Milo Brentwick Homes – Business Card</title>
<link href="https://fonts.googleapis.com/css2?family=Tinos:wght@400;700&display=swap" rel="stylesheet">
<style>
  :root{
    --canvas:#e9e6e1;
    --navy-deep:#1b2580;
    --navy-mid:#2a3aa6;
    --navy-light:#3d57c4;
    --brand-blue:#0455a3;
    --name-blue:#1f3f93;
    --brand-red:#ec1f27;
    --text-gray:#50535a;
    --white:#ffffff;
    --photo-dark:#3a3d44;
    --photo-light:#d9d4cf;
  }
  *{box-sizing:border-box;margin:0;padding:0}
  html,body{width:1200px;height:950px;overflow:hidden}
  body{background:var(--canvas);font-family:"Tinos","Times New Roman",serif;position:relative}

  .card{position:absolute;left:250px;width:700px;height:400px;overflow:hidden;box-shadow:0 10px 30px rgba(0,0,0,.25)}
  .card--back{top:30px;background:radial-gradient(ellipse at 60% 40%,var(--navy-light) 0%,var(--navy-mid) 45%,var(--navy-deep) 100%)}
  .card--front{top:500px;background:var(--white)}

  /* back */
  .back-brand{position:absolute;left:0;right:0;top:150px;display:flex;align-items:center;justify-content:center;gap:16px;color:var(--white)}
  .back-brand .mark{width:54px;height:54px;border:3px solid var(--white);border-radius:50%}
  .back-brand .wordmark{font-size:40px;font-weight:400;letter-spacing:1px;line-height:1}
  .back-brand .wordmark small{display:block;font-size:15px;letter-spacing:7px;margin-top:6px;text-align:right}
  .back-web{position:absolute;left:0;right:0;top:300px;text-align:center;color:var(--white);font-size:15px;letter-spacing:5px}

  /* front */
  .front-brand{position:absolute;left:42px;top:54px;display:flex;align-items:center;gap:10px}
  .front-brand .mark{width:40px;height:40px;border:3px solid var(--brand-red);border-radius:50%}
  .front-brand .wordmark{font-size:28px;color:var(--brand-blue);line-height:1}
  .front-brand .wordmark small{display:block;font-size:11px;letter-spacing:5px;margin-top:4px;text-align:right}

  .agent{position:absolute;left:46px;top:126px}
  .agent-name{font-size:24px;font-weight:700;color:var(--name-blue);line-height:1.1}
  .agent-title{font-size:16px;color:var(--brand-red);margin-top:2px}
  .address{font-size:16px;color:var(--text-gray);margin-top:6px;line-height:1.3}
  .address .badge{display:inline-block;width:34px;height:14px;background:#c9d8ee;border:1px solid #8fa9d6;vertical-align:middle;margin-left:6px}

  .contacts{list-style:none;margin-top:4px}
  .contacts li{display:flex;align-items:center;gap:10px;font-size:16px;color:var(--text-gray);line-height:1.4}
  .contacts svg{width:15px;height:15px;fill:var(--name-blue);flex:none}

  .agent-photo{position:absolute;right:0;top:0;width:290px;height:330px;
    background:linear-gradient(160deg,var(--photo-light) 0%,#b9a79a 45%,var(--photo-dark) 100%);
    clip-path:polygon(0 0,100% 0,100% 82%,0 100%)}

  .front-bands{position:absolute;left:0;bottom:0;width:700px;height:140px}
</style>
</head>
<body>

  <section class="card card--back" aria-label="Card back">
    <div class="back-brand">
      <span class="mark"></span>
      <div class="wordmark">MILO BRENTWICK<small>HOMES</small></div>
    </div>
    <p class="back-web">www.website.com</p>
  </section>

  <section class="card card--front" aria-label="Card front">
    <div class="agent-photo" role="img" aria-label="Portrait photo of the agent in a dark suit"></div>

    <div class="front-brand">
      <span class="mark"></span>
      <div class="wordmark">MILO BRENTWICK<small>HOMES</small></div>
    </div>

    <div class="agent">
      <h1 class="agent-name">Milo Brentwick</h1>
      <p class="agent-title">Realtor, MBA, MPH</p>
      <p class="address">24 Alderwood court fairhaven<br>Oregon 97402<span class="badge"></span></p>
      <ul class="contacts">
        <li><svg viewBox="0 0 16 16"><path d="M3 1h3l1 4-2 1a9 9 0 0 0 5 5l1-2 4 1v3c0 1-1 2-2 2A13 13 0 0 1 1 3c0-1 1-2 2-2z"/></svg>555.210.4080</li>
        <li><svg viewBox="0 0 16 16"><path d="M4 0h8a1 1 0 0 1 1 1v14a1 1 0 0 1-1 1H4a1 1 0 0 1-1-1V1a1 1 0 0 1 1-1zm1 2v10h6V2z"/></svg>555.318.6241</li>
        <li><svg viewBox="0 0 16 16"><path d="M4 0h7v5H4zM1 6h14v8H1zm3 2v2h8V8z"/></svg>555.210.4087</li>
        <li><svg viewBox="0 0 16 16"><path d="M0 3h16v10H0zm1 1 7 5 7-5z"/></svg>Milo@MiloBrentwickHomes.com</li>
      </ul>
    </div>

    <svg class="front-bands" viewBox="0 0 700 140" preserveAspectRatio="none" aria-hidden="true">
      <path d="M410 140 L410 130 L700 78 L700 140Z" fill="var(--brand-blue)"/>
      <path d="M0 124 L700 72 L700 77 L0 129Z" fill="var(--brand-red)"/>
      <path d="M0 133 L700 84 L700 140 L0 140Z" fill="var(--brand-blue)"/>
      <path d="M0 134 L700 128 L700 131 L0 137Z" fill="var(--brand-red)"/>
    </svg>
  </section>

</body>
</html>
```